Covid-19 Mortgage Housing Market Coaching

I need a one page 8.5 x 11 printable infographic to describe the following:
Housing and Mortgage Market Coach
Through your Employer Home-ownership Benefit
The Coronavirus has resulted in an unprecedented Government coordination to reduce the spread of the virus, as such, has altered the way we live and work.
As each of us looks to the potential impact of the Coronavirus to our financial stability, it can be difficult to obtain trusted information to help make sound financial decisions.
As part of your employee home ownership program through your employer, you have access to this educational coaching on the below topics:
• What is happening in the stock market and why it is happening.
• Motivation behind Feds cutting rates and how that translates to the lending market.
• Discuss the future of interest rates.
• Discuss the future of the housing market. How will the spring and summer housing markets be effected?
• Everyone says to refinance now. Is that really in my best interest? Learn how to do a refinance analysis and determine if refinancing is right for you.
Having a better understanding of what is happening in the financial markets, with interest rates and the housing market can help you successfully navigate this rapidly evolving situation.
Please be sure that our phone number is prominently displayed 1-800-529-8172 and our web address www.brightkeylending.example

```html
<!DOCTYPE html>
<html lang="en">
<head>
<meta charset="utf-8">
<title>Market Coach – Housing | Mortgage</title>
<link rel="stylesheet" href="https://fonts.googleapis.com/css2?family=Bebas+Neue&family=Open+Sans:wght@400;600&display=swap">
<style>
  :root {
    --navy: #1f3a68;
    --green: #2e8b3e;
    --leaf: #5cb547;
    --grey-text: #55595e;
    --paper: #ffffff;
    --backdrop: #3a3839;
  }
  * { margin: 0; padding: 0; box-sizing: border-box; }
  html, body { width: 1200px; height: 2400px; overflow: hidden; background: var(--backdrop); }
  .flyer {
    position: absolute; left: 50px; top: 488px;
    width: 1100px; height: 1424px;
    overflow: hidden;
    background: var(--paper);
    box-shadow: 0 6px 18px rgba(0,0,0,.45);
    font-family: "Open Sans", sans-serif;
  }
  .masthead { position: absolute; top: 86px; left: 0; width: 100%; text-align: center; font-family: "Bebas Neue", sans-serif; }
  .masthead__title { color: var(--navy); font-size: 68px; line-height: 64px; letter-spacing: 22px; padding-left: 22px; font-weight: 400; }
  .masthead__sub { display: inline-block; color: var(--green); font-size: 46px; line-height: 46px; letter-spacing: 14px; margin-top: 10px; padding-left: 14px; padding-bottom: 4px; border-bottom: 2px solid var(--green); }
  .masthead__tag { color: var(--green); font-size: 21px; letter-spacing: 4.4px; margin-top: 6px; }
  .copy { position: absolute; left: 71px; width: 940px; font-size: 16.5px; line-height: 22px; letter-spacing: 2.1px; text-align: justify; }
  .copy--intro { top: 343px; color: var(--navy); font-weight: 600; }
  .copy--access { top: 492px; color: var(--green); font-weight: 600; }
  .copy--close { top: 739px; color: var(--green); font-weight: 600; }
  .topics { position: absolute; top: 578px; left: 84px; width: 920px; list-style: none; color: var(--grey-text); font-size: 14.5px; line-height: 19px; letter-spacing: 1.5px; }
  .topics li { position: relative; padding-left: 16px; margin-bottom: 3px; }
  .topics li::before { content: ""; position: absolute; left: 0; top: 7px; width: 6px; height: 6px; border-radius: 50%; background: var(--green); }
  .hero-art { position: absolute; left: 44px; top: 822px; width: 1012px; height: 430px; border-radius: 4px;
    background: linear-gradient(100deg, #ffffff 0%, #5cb547 18%, #3f9e3a 45%, #d9d9d9 65%, #f2f2f2 100%); opacity: .85; }
  .brand { position: absolute; left: 28px; top: 1272px; }
  .brand__name { display: flex; align-items: center; gap: 10px; color: var(--navy); font-size: 28px; font-weight: 600; letter-spacing: -.5px; }
  .brand__mark { width: 18px; height: 18px; background: var(--leaf); }
  .brand__line { color: var(--navy); font-size: 14px; margin-left: 28px; margin-top: 2px; }
  .contact { position: absolute; left: 640px; top: 1282px; width: 430px; color: var(--green); font-size: 21px; line-height: 31px; letter-spacing: 2.4px; white-space: nowrap; }
  .contact__phone { letter-spacing: 4px; }
</style>
</head>
<body>
  <main class="flyer">
    <header class="masthead">
      <h1 class="masthead__title">Market Coach</h1>
      <div class="masthead__sub">Housing | Mortgage</div>
      <p class="masthead__tag">Through your employer home-ownership benefit</p>
    </header>

    <p class="copy copy--intro">The Coronavirus has resulted in an unprecedented Government coordination to reduce the spread of the virus, as such, has altered the way we live and work.<br>As each of us looks to the potential impact of the Coronavirus to our financial stability, it can be difficult to obtain trusted information to help make sound financial decisions.</p>

    <p class="copy copy--access">As part of your employee home ownership program through your employer, you have access to this educational coaching on the below topics:</p>

    <ul class="topics">
      <li>What is happening in the stock market and why it is happening.</li>
      <li>Motivation behind Feds cutting rates and how that translates to the lending market.</li>
      <li>Discuss the future of interest rates.</li>
      <li>Discuss the future of the housing market. How will the spring and summer housing markets be effected?</li>
      <li>Everyone says to refinance now. Is that really in my best interest? Learn how to do a refinance analysis and determine if refinancing is right for you.</li>
    </ul>

    <p class="copy copy--close">Having a better understanding of what is happening in the financial markets, with interest rates and the housing market can help you successfully navigate this rapidly evolving situation.</p>

    <div class="hero-art" role="img" aria-label="Illustration of a row of green paper houses and one large grey house, each with a virus particle rolling in front of it"></div>

    <div class="brand">
      <div class="brand__name"><span class="brand__mark"></span>BrightKey Lending</div>
      <div class="brand__line">Employee Home Ownership Program</div>
    </div>

    <div class="contact">
      <div class="contact__phone">1-800-529-8172</div>
      <div class="contact__web">www.brightkeylending.example</div>
    </div>
  </main>
</body>
</html>
```